Tavix-Commodities. Limestone; improving the world

New Limestone company and need logo design.
Limestone offsets carbon mitigation industries restore and replenish soil fertilities in the Prairies, the breadbasket of the world. At the same time, Limestone is proving a critical emergent component of carbon capture sequestration technology will therefore play a critical role in the development of the western Canadian energy industries
Our limestone resources are situated in the foothills of the Canadian Rockies well-positioned above the sprawling fields of the vast peace district.
Target Market(s)
Agriculture and oli sites
Logo Text
Tavix Commodities
Number of Pages Required
3 page

```html
<!DOCTYPE html>
<html lang="en">
<head>
<meta charset="utf-8">
<title>Tavix Commodities — Home</title>
<link href="https://fonts.googleapis.com/css2?family=Fira+Sans:wght@400;500;600;700&family=Montserrat:wght@900&display=swap" rel="stylesheet">
<style>
:root{
  --backdrop:#4d4d4d;
  --page:#ffffff;
  --teal:#0399a6;
  --teal-ink:#0a8e9b;
  --deep:#003a3c;
  --panel:#f1f1f1;
  --body-ink:#4a4a4a;
  --white:#ffffff;
}
*{margin:0;padding:0;box-sizing:border-box}
html,body{width:790px;height:1200px;overflow:hidden}
body{background:var(--backdrop);font-family:"Fira Sans",Arial,sans-serif;position:relative}
.page{position:absolute;left:73px;top:18px;width:643px;height:1164px;background:var(--page);overflow:hidden}
.abs{position:absolute}

/* header */
.util-link{left:475px;top:10px;font-size:5px;font-weight:500;color:var(--deep)}
.portal-btn{left:513px;top:6px;width:55px;height:13px;border-radius:7px;background:var(--deep);color:var(--white);font-size:5px;font-weight:500;display:flex;align-items:center;justify-content:center}
.brand{left:17px;top:21px;color:var(--teal);font-weight:700;line-height:1}
.brand .word-main{display:block;font-size:20px;letter-spacing:.2px}
.brand .word-sub{display:block;font-size:9px;margin-top:1px}
.nav-bar{left:96px;top:28px;width:547px;height:16px;background:var(--teal)}
.nav-item{top:34px;font-size:5px;color:var(--white);letter-spacing:.1px}
.search-icon{left:543px;top:32px;width:8px;height:8px}
.search-field{left:552px;top:33px;width:52px;height:6px;border-radius:3px;background:var(--white)}

/* hero */
.hero-frame{left:69px;top:74px;width:504px;height:168px;background:var(--deep)}
.hero-panel{left:76px;top:68px;width:490px;height:167px;background:var(--panel)}
.hero-art{left:115px;top:92px;width:167px;height:104px;border-radius:84px 84px 30px 40px;background:radial-gradient(circle at 50% 40%,#7fd79a 0%,#3fb36a 55%,#1f8f4e 100%)}
.hero-title{left:346px;top:95px;font-family:"Montserrat",Arial,sans-serif;font-weight:900;font-size:29px;line-height:34px;color:var(--deep)}

/* intro columns */
.sec-head{font-size:9.5px;font-weight:600;color:var(--teal-ink)}
.copy{font-size:5px;line-height:6.75px;color:var(--body-ink)}
.col-divider{left:209px;top:271px;width:1px;height:228px;background:var(--deep)}
.photo-forest{left:446px;top:285px;width:151px;height:196px;background:linear-gradient(160deg,#1c3b27 0%,#2f6a34 45%,#4f9a3a 70%,#183420 100%)}

/* feature row */
.photo-site{left:29px;top:544px;width:294px;height:165px;background:linear-gradient(135deg,#3b3222 0%,#6b5a33 40%,#4a4028 70%,#2c2618 100%)}
.arrow{width:26px;height:10px}

/* footer */
.footer-links{top:758px;left:0;width:643px;height:139px;background:var(--deep)}
.foot-col{top:28px;list-style:none;font-size:5.2px;line-height:9.9px;color:var(--white)}
.foot-col li:first-child{font-weight:500}
.footer-band{top:897px;left:0;width:643px;height:267px;background:var(--teal)}
.footer-brand{left:0;top:110px;width:643px;text-align:center;color:var(--white);font-weight:700;line-height:1}
.footer-brand .word-main{display:block;font-size:38px}
.footer-brand .word-sub{display:block;font-size:17px;margin-top:2px}
</style>
</head>
<body>
<div class="page">
  <header>
    <a class="abs util-link">Contact Us</a>
    <a class="abs portal-btn">Customer Portal</a>
    <div class="abs brand"><span class="word-main">Tavix</span><span class="word-sub">Commodities</span></div>
    <nav>
      <div class="abs nav-bar"></div>
      <span class="abs nav-item" style="left:159px">PRODUCTS</span>
      <span class="abs nav-item" style="left:212px">MARKETS</span>
      <span class="abs nav-item" style="left:263px">LOCATIONS</span>
      <span class="abs nav-item" style="left:311px">SUSTAINABILITY</span>
      <span class="abs nav-item" style="left:381px">ABOUT US</span>
      <span class="abs nav-item" style="left:434px">CAREERS</span>
      <svg class="abs search-icon" viewBox="0 0 8 8"><circle cx="3.2" cy="3.2" r="2.2" fill="none" stroke="#fff" stroke-width=".8"/><line x1="4.8" y1="4.8" x2="7.2" y2="7.2" stroke="#fff" stroke-width=".9"/></svg>
      <div class="abs search-field"></div>
    </nav>
  </header>

  <section class="hero">
    <div class="abs hero-frame"></div>
    <div class="abs hero-panel"></div>
    <div class="abs hero-art" role="img" aria-label="Green paper-cut landscape with wind turbines, houses, trees, clouds and sun"></div>
    <h1 class="abs hero-title">Lorem<br>ipsum dolor<br>sit amet</h1>
  </section>

  <section class="intro">
    <h2 class="abs sec-head" style="left:41px;top:280px">Lorem ipsum</h2>
    <p class="abs copy" style="left:41px;top:302px;width:141px">Lorem ipsum dolor sit amet, consectetuer adipiscing elit, sed diam nonummy nibh euismod tincidunt ut laoreet dolore magna aliquam erat volutpat. Ut wisi enim ad minim veniam, quis nostrud exerci tation ullamcorper suscipit lobortis nisl ut aliquip ex ea commodo consequat. Duis autem vel eum iriure dolor in hendrerit in vulputate velit esse molestie consequat, vel illum dolore eu feugiat nulla facilisis at vero eros et accumsan et iusto odio dignissim qui blandit praesent luptatum zzril delenit augue duis dolore te feugait nulla facilisi.<br>Lorem ipsum dolor sit amet, cons ectetuer adipiscing elit, sed diam nonummy nibh euismod tincidunt ut laoreet Lorem ipsum dolor sit amet, consectetuer adipiscing elit, sed diam nonummy nibh euismod tincidunt ut laoreet dolore magna aliquam erat volutpat. Ut wisi enim ad minim veniam, quis nostrud exerci tation ullamcorper suscipit lobortis nisl ut aliquip ex ea commodo consequat. Duis autem vel eum iriure dolor in hendrerit in vulputate velit esse molestie consequat, vel illum dolore eu feugiat nulla facilisis at vero eros et accumsan et iusto odio dignissim qui blandit praesent Lorem ipsum dolor sit amet, consectetuer adipiscing elit, sed diam nonummy nibh euismod tincidunt ut laoreet dolore magna</p>
    <div class="abs col-divider"></div>
    <h2 class="abs sec-head" style="left:249px;top:280px">Lorem ipsum</h2>
    <p class="abs copy" style="left:249px;top:302px;width:141px">Lorem ipsum dolor sit amet, consectetuer adipiscing elit, sed diam nonummy nibh euismod tincidunt ut laoreet dolore magna aliquam erat volutpat. Ut wisi enim ad minim veniam, quis nostrud exerci tation ullamcorper suscipit lobortis nisl ut aliquip ex ea commodo consequat. Duis autem vel eum iriure dolor in hendrerit in vulputate velit esse molestie consequat, vel illum dolore eu feugiat nulla facilisis at vero eros et accumsan et iusto odio dignissim qui blandit praesent luptatum zzril delenit augue duis dolore te feugait nulla facilisi.<br>Lorem ipsum dolor sit amet, cons ectetuer adipiscing elit, sed diam nonummy nibh euismod tincidunt ut laoreet dolore magna aliquam erat volutpat. Ut wisi enim ad minim veniam, quis nostrud exerci tation ullamcorper suscipit lobortis nisl ut aliquip ex ea commodo consequat.<br>Lorem ipsum dolor sit amet, consectetuer adipiscing elit, sed diam nonummy nibh euismod tincidunt ut laoreet dolore magna aliquam erat volutpat. Ut wisi enim ad minim veniam, quis nostrud exerci tation ullamcorper suscipit lobortis nisl ut aliquip ex ea commodo consequat. Duis autem vel eum iriure dolor in hendrerit in vulputate velit esse molestie consequat, vel illum dolore eu feugiat nulla facilisis at vero eros et</p>
    <div class="abs photo-forest" role="img" aria-label="Aerial view of a dense green forest canopy"></div>
  </section>

  <section class="features">
    <div class="abs photo-site" role="img" aria-label="Aerial view of a quarry site with a truck and excavator on brown earth"></div>
    <h2 class="abs sec-head" style="left:355px;top:551px">Lorem ipsum</h2>
    <p class="abs copy" style="left:355px;top:567px;width:234px">Lorem ipsum dolor sit amet, consectetuer adipiscing elit, sed diam nonummy nibh euismod tincidunt ut laoreet dolore magna aliquam erat volutpat. Ut wisi enim ad minim veniam, quis nostrud exerci tation ullamcorper suscipit lobortis nisl ut aliquip ex ea commodo consequat. Duis autem vel eum iriure dolor in hendrerit in vulputate velit esse molestie consequat, vel illum dolore eu feugiat nulla facilisis at vero eros et accumsan et iusto odio dignissim qui blandit praesent luptatum zzril delenit augue duis dolore te feugait nulla facilisi.</p>
    <svg class="abs arrow" style="left:550px;top:618px" viewBox="0 0 26 10"><line x1="0" y1="5" x2="25" y2="5" stroke="#0399a6" stroke-width=".8"/><polyline points="20,1 25,5 20,9" fill="none" stroke="#0399a6" stroke-width=".8"/></svg>
    <h2 class="abs sec-head" style="left:355px;top:638px">Lorem ipsum</h2>
    <p class="abs copy" style="left:355px;top:654px;width:234px">Lorem ipsum dolor sit amet, consectetuer adipiscing elit, sed diam nonummy nibh euismod tincidunt ut laoreet dolore magna aliquam erat volutpat. Ut wisi enim ad minim veniam, quis nostrud exerci tation ullamcorper suscipit lobortis nisl ut aliquip ex ea commodo consequat. Duis autem vel eum iriure dolor in hendrerit in vulputate velit esse molestie consequat, vel illum dolore eu feugiat nulla facilisis at vero eros et accumsan et iusto odio dignissim qui blandit praesent luptatum zzril delenit augue duis dolore te feugait nulla facilisi.</p>
    <svg class="abs arrow" style="left:550px;top:702px" viewBox="0 0 26 10"><line x1="0" y1="5" x2="25" y2="5" stroke="#0399a6" stroke-width=".8"/><polyline points="20,1 25,5 20,9" fill="none" stroke="#0399a6" stroke-width=".8"/></svg>
  </section>

  <footer>
    <div class="abs footer-links">
      <ul class="abs foot-col" style="left:38px"><li>HOME</li><li>CUSTOMER PORTAL</li><li>WHAT IS LIME?</li><li>NEWS</li><li>CONTACT US</li></ul>
      <ul class="abs foot-col" style="left:147px"><li>PRODUCTS</li><li>Quicklime</li><li>Hydrated Lime</li><li>Pulverized Limestone</li><li>Chemical Limestone</li><li>Construction Stone</li><li>Co-products</li><li>Safety Data Sheets (SDS)</li><li>Technical Information</li></ul>
      <ul class="abs foot-col" style="left:232px"><li>MARKETS</li><li>Mining</li><li>Steel</li><li>Environmental</li><li>Pulp &amp; Paper</li><li>Glass</li><li>Agriculture</li><li>Food</li><li>Building Construction</li><li>Construction Materials</li></ul>
      <ul class="abs foot-col" style="left:308px"><li>LOCATIONS</li><li>Location Map</li><li>North America</li><li>Asia Pacific</li><li>Corporate Office</li><li>Regional offices</li><li>Lime</li><li>Terminals</li><li>Grupo Veralta</li></ul>
      <ul class="abs foot-col" style="left:371px"><li>SUSTAINABILITY</li><li>Our Commitment</li><li>Environmental Care</li><li>Workforce Culture</li><li>Community Relations</li><li>Transparency</li><li>Sustainability Reports</li><li>COVID-19</li></ul>
      <ul class="abs foot-col" style="left:451px"><li>ABOUT US</li><li>Who We Are</li><li>Mission, Vision &amp; Values</li><li>Strategic Leadership Team</li><li>Workforce Culture</li><li>Customer Services</li><li>Brochures</li></ul>
      <ul class="abs foot-col" style="left:537px"><li>CAREERS</li><li>A Great Place to Work</li><li>Job Openings</li></ul>
    </div>
    <div class="abs footer-band">
      <div class="abs footer-brand"><span class="word-main">Tavix</span><span class="word-sub">Commodities</span></div>
    </div>
  </footer>
</div>
</body>
</html>
```